Develop a Corporate Identity for VELO brand

VELO is a range of Car Care, Home Care, Floor Care, Personal Care and Industrial Care products. The tagline is VELO Price, VELO Quality, VELO Value. The logo has been designed already and is attached. The logo and name is a trade mark in South Africa.

A marketing campaign will be launched to get the products on the shelves of wholesalers and retailers. Photos of the products are attached.

VELO Direct is the name of a shop that is setup for customers to view and buy the products. A facebook page has been setup ([url removed, login to view]) and a twitter account ([url removed, login to view]) is available. Other social media profiles will be setup.

During this contest a corporate identity will be designed for this brand of detergents. It will consist of: business cards, letterhead, email signature, presentation folder, brochure layout, powerpoint template, apparel design, indoor and outdoor signage and delivery vehicle branding. The existing logo will be used for the corporate identity. The colour combinations can be changed as per the attached photos of products.

```html
<!DOCTYPE html>
<html lang="en">
<head>
<meta charset="utf-8">
<title>VELO Business Cards</title>
<link rel="stylesheet" href="https://fonts.googleapis.com/css2?family=Open+Sans:wght@400;600&display=swap">
<style>
  :root {
    --backdrop: #e9e7e3;
    --card: #ffffff;
    --brand-red: #d7262f;
    --brand-green: #3f9a45;
    --ink: #333333;
    --on-green: #ffffff;
  }
  * { box-sizing: border-box; margin: 0; padding: 0; }
  html, body { width: 1200px; height: 900px; overflow: hidden; }
  body {
    background: var(--backdrop);
    font-family: "Open Sans", Arial, sans-serif;
    position: relative;
  }
  .card {
    position: absolute;
    width: 540px;
    height: 310px;
    background: var(--card);
    border-radius: 16px;
    overflow: hidden;
    box-shadow: 0 6px 18px rgba(0,0,0,0.12);
  }
  .card-front { left: 40px; top: 130px; }
  .card-back { left: 620px; top: 460px; }

  .brand-name {
    position: absolute;
    color: var(--ink);
    font-family: "Open Sans", Arial, sans-serif;
    font-weight: 400;
    line-height: 1;
    letter-spacing: 2px;
  }
  .card-front .brand-name { font-size: 60px; left: 0; right: 0; top: 100px; text-align: center; }
  .tagline {
    position: absolute;
    left: 0; right: 0; top: 214px;
    text-align: center;
    color: var(--brand-red);
    font-size: 17px;
    font-weight: 400;
    letter-spacing: 0.3px;
  }

  .card-back .brand-name { font-size: 38px; left: 44px; top: 128px; }
  .card-band { position: absolute; inset: 0; }
  .holder { position: absolute; right: 36px; top: 30px; text-align: right; }
  .holder-name { color: var(--ink); font-size: 20px; font-weight: 400; }
  .holder-role { color: var(--brand-red); font-size: 12px; font-weight: 600; margin-top: 2px; }

  .contact {
    position: absolute;
    display: flex;
    align-items: center;
    gap: 12px;
    color: var(--on-green);
    font-size: 13px;
  }
  .contact svg { width: 16px; height: 16px; flex: none; }
  .contact-phone { left: 34px; top: 246px; }
  .contact-email { left: 34px; top: 276px; }
  .contact-address { left: 372px; top: 186px; }
  .contact-web { left: 372px; top: 216px; }
</style>
</head>
<body>

  <section class="card card-front">
    <div class="brand-name">VELO</div>
    <p class="tagline">VELO Price, VELO Quality, VELO Value</p>
  </section>

  <section class="card card-back">
    <svg class="card-band" viewBox="0 0 540 310" width="540" height="310" aria-hidden="true">
      <path d="M0 232 Q 300 205 540 84 L540 310 L0 310 Z" fill="var(--brand-green)"/>
      <path d="M0 222 Q 300 195 540 74" fill="none" stroke="var(--brand-red)" stroke-width="2"/>
    </svg>

    <div class="holder">
      <div class="holder-name">Daniel Marsh</div>
      <div class="holder-role">Manager</div>
    </div>

    <div class="brand-name">VELO</div>

    <div class="contact contact-phone">
      <svg viewBox="0 0 16 16" aria-hidden="true"><path d="M3 1.5l2.5 0 1.2 3.2-1.6 1.2c.8 1.8 2.2 3.2 4 4l1.2-1.6 3.2 1.2v2.5c0 .8-.7 1.5-1.5 1.5C6.4 13.5 2.5 9.6 1.5 3 1.5 2.2 2.2 1.5 3 1.5z" fill="currentColor"/></svg>
      <span>021-555-0147</span>
    </div>
    <div class="contact contact-email">
      <svg viewBox="0 0 16 16" aria-hidden="true"><rect x="1" y="3" width="14" height="10" rx="1" fill="none" stroke="currentColor" stroke-width="1.5"/><path d="M1.5 3.8L8 9l6.5-5.2" fill="none" stroke="currentColor" stroke-width="1.5"/></svg>
      <span>danielmarsh@velodirect.com</span>
    </div>
    <div class="contact contact-address">
      <svg viewBox="0 0 16 16" aria-hidden="true"><path d="M8 1a5 5 0 0 0-5 5c0 3.6 5 9 5 9s5-5.4 5-9a5 5 0 0 0-5-5zm0 7a2 2 0 1 1 0-4 2 2 0 0 1 0 4z" fill="currentColor"/></svg>
      <span>Address Here</span>
    </div>
    <div class="contact contact-web">
      <svg viewBox="0 0 16 16" aria-hidden="true"><rect x="1" y="5" width="7" height="6" rx="2" fill="none" stroke="currentColor" stroke-width="1.5"/><rect x="8" y="5" width="7" height="6" rx="2" fill="none" stroke="currentColor" stroke-width="1.5"/></svg>
      <span>www.velodirect.com</span>
    </div>
  </section>

</body>
</html>
```